Professional individual needs business card design

I need a business card designed for my friend to show their skills and contact details

I would like to see pattern designs with a black foreground and strong look - will submit content specifics but basics are:

NAME SURNAME (large and bold)
Event Manager & MC

Velvet Harbour
The other event I run

phone number - email

```html
<!DOCTYPE html>
<html lang="en">
<head>
<meta charset="utf-8">
<title>Business Card – Name Surname</title>
<link href="https://fonts.googleapis.com/css2?family=Open+Sans:wght@400;600;700&family=Roboto+Condensed:wght@300;700&display=swap" rel="stylesheet">
<style>
  :root {
    --page-bg: #8a8a8a;
    --card-bg: #1b1b1b;
    --card-tone-dark: #161616;
    --card-tone-light: #232323;
    --rule: rgba(255, 255, 255, 0.05);
    --ink: #ffffff;
  }
  * { margin: 0; padding: 0; box-sizing: border-box; }
  html, body {
    width: 1200px;
    height: 1200px;
    overflow: hidden;
    background: var(--page-bg);
  }
  .canvas {
    position: relative;
    width: 1200px;
    height: 1200px;
  }
  .card {
    position: absolute;
    left: 100px;
    top: 316px;
    width: 1000px;
    height: 568px;
    background: var(--card-bg);
    overflow: hidden;
    color: var(--ink);
    font-family: "Open Sans", sans-serif;
  }
  .card-texture {
    position: absolute;
    inset: 0;
    background: radial-gradient(ellipse at 45% 50%, var(--card-tone-light) 0%, var(--card-bg) 55%, var(--card-tone-dark) 100%);
  }
  .band {
    position: absolute;
    left: 90px;
    right: 120px;
    height: 1px;
    background: var(--rule);
  }
  .divider {
    position: absolute;
    left: 495px;
    top: 92px;
    width: 2px;
    height: 383px;
    background: rgba(0, 0, 0, 0.35);
    box-shadow: 1px 0 0 var(--rule);
  }
  .identity {
    position: absolute;
    left: 73px;
    width: 400px;
    top: 240px;
    text-align: center;
  }
  .identity-name {
    font-family: "Roboto Condensed", sans-serif;
    font-size: 42px;
    line-height: 1;
    letter-spacing: 0.5px;
  }
  .identity-name .first { font-weight: 300; }
  .identity-name .last { font-weight: 700; }
  .identity-role {
    margin-top: 10px;
    font-size: 19px;
    font-weight: 400;
  }
  .brand {
    position: absolute;
    left: 569px;
    top: 138px;
    font-size: 24px;
    font-weight: 700;
    letter-spacing: 1px;
  }
  .contact {
    position: absolute;
    left: 569px;
    display: flex;
    align-items: center;
    gap: 20px;
    font-size: 18px;
    line-height: 25px;
    white-space: nowrap;
  }
  .contact svg { flex: none; fill: var(--ink); }
  .contact-email { top: 222px; }
  .contact-phone { top: 290px; }
  .contact-address { top: 370px; }
</style>
</head>
<body>
<div class="canvas">
  <div class="card">
    <div class="card-texture" role="img" aria-label="Subtle faceted diamond pattern in dark charcoal tones"></div>
    <div class="band" style="top:92px"></div>
    <div class="band" style="top:219px"></div>
    <div class="band" style="top:347px"></div>
    <div class="band" style="top:475px"></div>
    <div class="divider"></div>

    <div class="identity">
      <div class="identity-name"><span class="first">NAME</span> <span class="last">SURNAME</span></div>
      <div class="identity-role">EVENT MANAGER &amp; MC</div>
    </div>

    <div class="brand">VELVET HARBOUR</div>

    <div class="contact contact-email">
      <svg width="28" height="18" viewBox="0 0 28 18" aria-hidden="true">
        <path d="M0 0h28v18H0z M2 2l12 9 12-9" fill="none" stroke="#fff" stroke-width="2"/>
        <path d="M0 0l14 10L28 0z"/>
        <path d="M0 18l10-8 M28 18l-10-8" stroke="#fff" stroke-width="2"/>
      </svg>
      <span>HELLO@VELVETHARBOUR.COM</span>
    </div>

    <div class="contact contact-phone">
      <svg width="28" height="28" viewBox="0 0 24 24" aria-hidden="true">
        <path d="M6.6 10.8a15 15 0 0 0 6.6 6.6l2.2-2.2a1 1 0 0 1 1-.25 11.4 11.4 0 0 0 3.6.57 1 1 0 0 1 1 1V20a1 1 0 0 1-1 1A17 17 0 0 1 3 4a1 1 0 0 1 1-1h3.5a1 1 0 0 1 1 1c0 1.25.2 2.45.57 3.57a1 1 0 0 1-.25 1z"/>
      </svg>
      <span>+18 5512 3904 6621<br>+18 6730 2458 1937</span>
    </div>

    <div class="contact contact-address">
      <svg width="30" height="28" viewBox="0 0 30 28" aria-hidden="true">
        <path d="M15 2L1 14h4v12h8v-8h4v8h8V14h4z"/>
      </svg>
      <span>14 ALDER QUAY ROAD<br>DOCKSIDE DISTRICT, NY, USA</span>
    </div>
  </div>
</div>
</body>
</html>
```